" A venda é feita porta á porta. Os produtos são divulgados nas redes sociais. O cliente faz contato e solicita uma visita. Um novo projeto esta sendo desenvolvido para montar uma loja móvel em uma van furgão. "

```html
<!DOCTYPE html>
<html lang="pt-BR">
<head>
<meta charset="UTF-8">
<title>Serena – Etiqueta</title>
<link href="https://fonts.googleapis.com/css2?family=Quicksand:wght@500;600;700&display=swap" rel="stylesheet">
<style>
  :root{
    --bg:#e9e8e8;
    --tag:#ffffff;
    --ink:#5e5454;
    --brand:#7b6c6c;
    --rose:#c9958a;
    --rose-light:#e8c9c1;
    --line:#e4d4d0;
    --icon:#b98f86;
  }
  *{box-sizing:border-box;margin:0;padding:0}
  html,body{width:1200px;height:1200px;overflow:hidden}
  body{background:var(--bg);font-family:'Quicksand',sans-serif;color:var(--ink);position:relative}
  .tag{
    position:absolute;top:150px;width:410px;height:960px;background:var(--tag);
    border-radius:22px;overflow:hidden;box-shadow:0 10px 28px rgba(0,0,0,.12);
  }
  .tag--front{left:175px}
  .tag--back{left:615px}
  .tag__hole{
    position:absolute;top:52px;left:50%;width:50px;height:50px;margin-left:-25px;
    border-radius:50%;background:var(--bg);box-shadow:inset 0 3px 6px rgba(0,0,0,.18);
  }
  .tag__band{
    position:absolute;left:0;right:0;bottom:0;height:62px;
    background:linear-gradient(90deg,var(--rose-light),var(--rose),var(--rose-light));
  }
  .brand{position:absolute;left:0;right:0;text-align:center}
  .brand__mark{display:block;margin:0 auto 14px;border-radius:50%;background:var(--rose)}
  .brand__name{font-weight:700;color:var(--brand);line-height:1}
  .brand__tagline{font-weight:600;color:var(--rose);letter-spacing:.18em}
  .tag--front .brand{top:400px}
  .tag--front .brand__mark{width:70px;height:70px}
  .tag--front .brand__name{font-size:78px}
  .tag--front .brand__tagline{font-size:19px;margin-top:8px}
  .contacts{position:absolute;left:38px;top:740px;list-style:none}
  .contacts li{display:flex;align-items:center;gap:14px;font-size:22px;font-weight:600;height:42px}
  .contacts__icon{width:28px;height:28px;border-radius:7px;background:var(--icon);display:flex;align-items:center;justify-content:center}
  .exchange{position:absolute;top:155px;left:0;right:0;text-align:center;font-size:23px;font-weight:600;line-height:1.4}
  .sizes{position:absolute;top:265px;left:28px;right:28px;display:flex;justify-content:space-between}
  .sizes span{
    width:50px;height:46px;border:2px solid var(--line);border-radius:9px;
    display:flex;align-items:center;justify-content:center;font-size:18px;font-weight:600;
  }
  .field{
    position:absolute;left:28px;right:28px;height:52px;border:2px solid var(--line);border-radius:10px;
    padding-left:12px;display:flex;align-items:center;font-size:21px;font-weight:600;
  }
  .field--ref{top:338px}
  .field--price{top:406px}
  .tag--back .brand{top:580px}
  .tag--back .brand__mark{width:52px;height:52px;margin-bottom:10px}
  .tag--back .brand__name{font-size:54px}
  .tag--back .brand__tagline{font-size:14px;margin-top:6px}
  .motto{position:absolute;top:775px;left:0;right:0;text-align:center;font-size:23px;font-weight:600;line-height:1.4}
</style>
</head>
<body>
  <article class="tag tag--front">
    <div class="tag__hole"></div>
    <div class="brand">
      <span class="brand__mark"></span>
      <div class="brand__name">Serena</div>
      <div class="brand__tagline">MODA E DEVOÇÃO</div>
    </div>
    <ul class="contacts">
      <li><span class="contacts__icon">
        <svg width="16" height="16" viewBox="0 0 24 24"><path fill="#fff" d="M6.6 10.8a15 15 0 0 0 6.6 6.6l2.2-2.2c.3-.3.7-.4 1-.2 1.1.4 2.3.6 3.6.6.6 0 1 .4 1 1V20c0 .6-.4 1-1 1A17 17 0 0 1 3 4c0-.6.4-1 1-1h3.5c.6 0 1 .4 1 1 0 1.3.2 2.5.6 3.6.1.3 0 .7-.2 1z"/></svg>
      </span>(27) 98140-3275</li>
      <li><span class="contacts__icon"></span>@serena.lojacatolica</li>
      <li><span class="contacts__icon"></span>/serena.lojacatolica</li>
    </ul>
    <div class="tag__band"></div>
  </article>

  <article class="tag tag--back">
    <div class="tag__hole"></div>
    <p class="exchange">Troca Somente com esta<br>etiqueta fixada na peça</p>
    <div class="sizes"><span>PP</span><span>P</span><span>M</span><span>G</span><span>GG</span><span>XG</span></div>
    <div class="field field--ref">Ref:</div>
    <div class="field field--price">R$:</div>
    <div class="brand">
      <span class="brand__mark"></span>
      <div class="brand__name">Serena</div>
      <div class="brand__tagline">MODA E DEVOÇÃO</div>
    </div>
    <p class="motto">“ Vista sua devoção e<br>compartilhe sua fé”.</p>
    <div class="tag__band"></div>
  </article>
</body>
</html>
```